BEACH CLUB OPENING INVITATION & FLYER DESIGN

Hi! I need a posh opening poster design for a new upscale beach club we are opening in Bodrum/Turkey. The text should be in english and turkish. Written text on the invitation and flyer should be:
Title: GRAND OPENING PARTY (Only written in English)
Date & Time: 28.05.2016 - 21:00
Address: Yelkenli Mahallesi Nergiz Sokak No: 3, Bodrum, Muğla / Türkiye
Website: www.lunorabeachclub.com
Email: info@lunorabeachclub.com
Tel: +90 (252) 647 18 25
Follow Us / Bizi Takip Edin
Snapwave: /lunorabeachclub
Friendnest: /lunorabeachclub
P.S: I attached the logo and some sample posters
Best of Luck

```html
<!DOCTYPE html>
<html lang="en">
<head>
<meta charset="utf-8">
<title>Lunora Beach Club – Grand Opening Party</title>
<link rel="stylesheet" href="https://fonts.googleapis.com/css2?family=Bungee&family=Oswald:wght@500&family=Lato:wght@400;700&display=swap">
<style>
  :root {
    --ink: #060606;
    --gold: #f2c81b;
    --gold-deep: #b98e0a;
    --white: #ffffff;
    --pink: #ee3762;
    --wine: #8e1f3f;
    --sky-top: #4a4a63;
    --sky-mid: #d9894a;
    --sky-glow: #fff1c2;
    --sea: #6e5a62;
  }
  * { box-sizing: border-box; margin: 0; padding: 0; }
  html, body { width: 907px; height: 1200px; overflow: hidden; background: var(--ink); }
  .flyer { position: relative; width: 907px; height: 1200px; overflow: hidden; background: var(--ink); font-family: "Lato", sans-serif; color: var(--white); }
  .artwork { position: absolute; inset: 0; }

  .brand { position: absolute; left: 20px; top: 470px; width: 220px; text-align: center; }
  .brand-dot { width: 46px; height: 46px; border-radius: 50%; background: var(--gold); margin: 0 auto 12px; }
  .brand-name { font-family: "Lato", sans-serif; font-weight: 700; font-size: 24px; color: var(--gold); letter-spacing: 1px; }

  .headline { position: absolute; left: 30px; top: 598px; font-family: "Bungee", sans-serif; line-height: 1; }
  .headline-main { font-size: 98px; letter-spacing: 2px;
    background: linear-gradient(180deg, var(--pink) 30%, var(--wine) 100%);
    -webkit-background-clip: text; background-clip: text; color: transparent; }
  .headline-sub { margin-top: 6px; font-size: 41px; color: var(--white); letter-spacing: 1px; }

  .date-label { position: absolute; left: 38px; top: 760px; font-size: 34px; }
  .date-line { position: absolute; left: 34px; top: 800px; display: flex; align-items: baseline; white-space: nowrap; }
  .date-day { font-family: "Oswald", sans-serif; font-weight: 500; font-size: 84px; line-height: 1;
    background: linear-gradient(180deg, #ffe24d 20%, var(--gold-deep) 100%);
    -webkit-background-clip: text; background-clip: text; color: transparent; }
  .date-year { font-weight: 700; font-size: 54px; margin-left: 10px; }
  .date-at { font-size: 38px; margin-left: 10px; }
  .date-time { font-weight: 700; font-size: 40px; margin-left: 10px; }

  .address { position: absolute; left: 38px; top: 906px; font-size: 22px; }

  .contacts { position: absolute; left: 40px; top: 968px; list-style: none; }
  .contacts li { display: flex; align-items: center; height: 30px; font-size: 17px; font-weight: 700; }
  .contact-icon { width: 18px; height: 18px; margin-right: 12px; flex: none; }
  .contact-icon.plain { background: var(--gold); border-radius: 3px; }
</style>
</head>
<body>
<main class="flyer">
  <svg class="artwork" width="907" height="1200" viewBox="0 0 907 1200">
    <defs>
      <linearGradient id="skyGrad" x1="0" y1="0" x2="0" y2="1">
        <stop offset="0" stop-color="var(--sky-top)"/>
        <stop offset="0.45" stop-color="var(--sky-mid)"/>
        <stop offset="0.7" stop-color="#b9786a"/>
        <stop offset="1" stop-color="var(--sea)"/>
      </linearGradient>
      <radialGradient id="sunGrad" cx="0.6" cy="0.15" r="0.5">
        <stop offset="0" stop-color="var(--sky-glow)"/>
        <stop offset="1" stop-color="var(--sky-glow)" stop-opacity="0"/>
      </radialGradient>
      <linearGradient id="poolGrad" x1="0" y1="0" x2="1" y2="1">
        <stop offset="0" stop-color="#4f7f92"/><stop offset="1" stop-color="#2b3d4c"/>
      </linearGradient>
      <linearGradient id="seaGrad" x1="0" y1="0" x2="0" y2="1">
        <stop offset="0" stop-color="#6c9ac8"/><stop offset="1" stop-color="#2c5e8c"/>
      </linearGradient>
      <linearGradient id="gardenGrad" x1="0" y1="0" x2="1" y2="1">
        <stop offset="0" stop-color="#e8e6dc"/><stop offset="1" stop-color="#4d6a3a"/>
      </linearGradient>
      <linearGradient id="maskGrad" x1="0" y1="0" x2="1" y2="1">
        <stop offset="0" stop-color="#f4f4f4"/><stop offset="0.6" stop-color="#bdbdbd"/><stop offset="1" stop-color="#8a8a8a"/>
      </linearGradient>
    </defs>

    <g role="img" aria-label="Photo: sunset over the sea framed by palm leaves">
      <rect x="0" y="0" width="907" height="600" fill="url(#skyGrad)"/>
      <rect x="0" y="0" width="907" height="600" fill="url(#sunGrad)"/>
    </g>

    <path d="M0,425 C170,415 300,505 470,512 C560,516 610,470 640,430 L907,560 L907,1200 L0,1200 Z" fill="var(--ink)"/>
    <path d="M0,412 C170,402 300,492 470,499 C560,503 610,457 640,417" fill="none" stroke="var(--white)" stroke-width="10"/>
    <path d="M0,421 C170,411 300,501 470,508 C560,512 610,466 640,426" fill="none" stroke="var(--gold)" stroke-width="5"/>

    <g role="img" aria-label="Photo: pair of masquerade masks on sand">
      <path d="M440,1200 C470,1090 520,1020 640,985 C760,950 790,870 907,830 L907,1200 Z" fill="url(#maskGrad)"/>
    </g>
    <path d="M440,1200 C470,1090 520,1020 640,985 C760,950 790,870 907,830" fill="none" stroke="var(--white)" stroke-width="12"/>
    <path d="M432,1200 C462,1084 514,1013 636,977 C756,942 786,862 907,821" fill="none" stroke="var(--gold)" stroke-width="5"/>

    <g role="img" aria-label="Photo: guest relaxing by the pool">
      <circle cx="730" cy="427" r="104" fill="url(#poolGrad)" stroke="var(--gold)" stroke-width="6"/>
    </g>
    <g role="img" aria-label="Photo: guest sitting at the seaside">
      <circle cx="617" cy="640" r="86" fill="url(#seaGrad)" stroke="var(--gold)" stroke-width="6"/>
    </g>
    <g role="img" aria-label="Photo: cabana lounger among plants">
      <circle cx="800" cy="609" r="100" fill="url(#gardenGrad)" stroke="var(--gold)" stroke-width="6"/>
    </g>
  </svg>

  <div class="brand">
    <div class="brand-dot"></div>
    <div class="brand-name">Lunora Beach Club</div>
  </div>

  <h1 class="headline">
    <div class="headline-main">GRAND</div>
    <div class="headline-sub">OPENING PARTY</div>
  </h1>

  <p class="date-label">Date &amp; Time:</p>
  <p class="date-line">
    <span class="date-day">28 TH MAY</span>
    <span class="date-year">2016</span>
    <span class="date-at">at</span>
    <span class="date-time">21:00</span>
  </p>

  <p class="address">Yelkenli Mahallesi Nergiz Sokak No: 3, Bodrum, Muğla</p>

  <ul class="contacts">
    <li>
      <svg class="contact-icon" viewBox="0 0 18 18" aria-hidden="true"><rect width="18" height="18" rx="3" fill="var(--gold)"/><path d="M5,4 L7.5,4 L8.5,6.5 L7,7.5 C7.8,9.2 8.8,10.2 10.5,11 L11.5,9.5 L14,10.5 L14,13 C9,13.5 4.5,9 5,4 Z" fill="var(--ink)"/></svg>
      +90 (252) 647 18 25
    </li>
    <li>
      <svg class="contact-icon" viewBox="0 0 18 18" aria-hidden="true"><rect x="1" y="4" width="16" height="11" rx="1" fill="var(--gold)"/><path d="M1,4.5 L9,10 L17,4.5" fill="none" stroke="var(--ink)" stroke-width="1.5"/></svg>
      info@lunorabeachclub.com
    </li>
    <li>
      <svg class="contact-icon" viewBox="0 0 18 18" aria-hidden="true"><circle cx="9" cy="9" r="8" fill="var(--gold)"/><path d="M1,9 H17 M9,1 C5,5 5,13 9,17 M9,1 C13,5 13,13 9,17" fill="none" stroke="var(--ink)" stroke-width="1.2"/></svg>
      www.lunorabeachclub.com
    </li>
    <li><span class="contact-icon plain"></span>/ Bizi Takip Edin</li>
    <li><span class="contact-icon plain"></span>Snapwave: /lunorabeachclub</li>
    <li><span class="contact-icon plain"></span>Friendnest: /lunorabeachclub</li>
  </ul>
</main>
</body>
</html>
```